business card for glass company

logo on business card and letterhead. our business is installing and servicing glass and mirror in commercial and industrial buildings in the Toronto area. full company name, Halworth Glass and Mirror Ltd.
i am looking for a business card and letterhead design.
on the letterhead i need company name and contact info
Halworth Glass and Mirror Ltd.
718 Larchmere Rd.
Toronto, Ontario
M4K 7B9
on the cards the contact info is
Dana Halworth
718 Larchmere Rd.
Toronto, Ontario
M4K 7B9
(416) 555-0142
(416) 555 0187-cell
i need another card with different name
Martin Quell
594 Kemble St. N
Hamilton Ontario
L3R 9T2
(416) 555-0142
(416) 555-0163
Target Market(s)
Professionals in industrial and commercial building construction, architects, general contractors, building managers and owners.
Industry/Entity Type
Business
Requirements
Must have
- simple design with two colors. emphasis on the name Halworth.

```html
<!DOCTYPE html>
<html lang="en">
<head>
<meta charset="utf-8">
<title>Halworth Glass &amp; Mirror Ltd. — Letterhead and Business Card</title>
<link rel="stylesheet" href="https://fonts.googleapis.com/css2?family=Orbitron:wght@700&display=swap">
<style>
  :root {
    --brand-blue: #0cb2e0;
    --band-top: #c4eefb;
    --band-card: #80e1f9;
    --sheet: #ffffff;
    --frame: #8a8a8a;
    --card-edge: #555555;
  }
  html, body {
    margin: 0;
    padding: 0;
    width: 1197px;
    height: 1200px;
    overflow: hidden;
    background: var(--sheet);
  }
  .canvas {
    position: relative;
    width: 1197px;
    height: 1200px;
    font-family: "Orbitron", sans-serif;
    font-weight: 700;
    color: var(--brand-blue);
  }
  .letterhead {
    position: absolute;
    left: 0;
    top: 0;
    width: 1186px;
    height: 1188px;
    border: 1px solid var(--frame);
    box-sizing: border-box;
    background: linear-gradient(to bottom, var(--band-top) 0, #ffffff 185px, #ffffff 100%);
  }
  .brand-name {
    position: absolute;
    margin: 0;
    line-height: 1;
    white-space: nowrap;
    font-weight: 700;
    color: var(--brand-blue);
  }
  .letterhead .brand-name {
    left: 60px;
    top: 98px;
    font-size: 50px;
  }
  .letterhead-address {
    position: absolute;
    right: 38px;
    top: 26px;
    margin: 0;
    text-align: right;
    font-size: 15px;
    line-height: 22px;
    font-style: normal;
    white-space: nowrap;
  }
  .business-card {
    position: absolute;
    left: 155px;
    top: 550px;
    width: 958px;
    height: 554px;
    border: 1px solid var(--card-edge);
    box-sizing: border-box;
    background: linear-gradient(to bottom, #ffffff 0, #ffffff 410px, var(--band-card) 470px, var(--band-card) 100%);
  }
  .business-card .brand-name {
    left: 70px;
    top: 196px;
    font-size: 94px;
  }
  .card-contact {
    position: absolute;
    left: 76px;
    top: 438px;
    margin: 0;
    font-style: normal;
  }
  .card-contact .person-name {
    display: block;
    font-size: 22px;
    line-height: 30px;
  }
  .card-contact .contact-line {
    display: block;
    font-size: 15px;
    line-height: 24px;
    white-space: nowrap;
  }
</style>
</head>
<body>
<div class="canvas">
  <section class="letterhead">
    <p class="brand-name">Halworth</p>
    <address class="letterhead-address">
      Halworth Glass &amp; Mirror ltd.<br>
      718 Larchmere Rd.<br>
      Toronto, Ontario<br>
      M4K 7B9
    </address>
  </section>

  <section class="business-card">
    <p class="brand-name">Halworth</p>
    <address class="card-contact">
      <span class="person-name">Dana Halworth</span>
      <span class="contact-line">718 Larchmere Rd. Toronto, Ontario, M4K 7B9</span>
      <span class="contact-line">(416) 555 0142 &nbsp;- &nbsp;(416) 555 0187-cell</span>
    </address>
  </section>
</div>
</body>
</html>
```